Group training gym/bootcamp needs a web design

We need a website for our gym that is based in Sydney. We have indoor functional training classes and outdoor bootcamp classes. We would like the web site to have a video (to be created) and photo gallery. I would like the site made on word press and i would like to be able to make minor changes such as changing images and text without having to use a designer.

The website should have the following pages: home page; the gym; the bootcamp; photo gallery; about us; contact.

I have uploaded our logo and i would like to keep to these colour (blue,yellow,silver) and black is also allowed

Target Market(s)

18-50 male and female

Industry/Entity Type

Gym

Coding

Coded - Design and coding required

Number of Pages Required

5+ page

Font styles to use
Sans Serif

Colors
0692cd
fbed22
1b1b1b
e8e8e8

Requirements
Must have
• The website should have the following pages: home page; the gym; the bootcamp; photo gallery; about us; contact.
• I have uploaded our logo and i would like to keep to these colour (blue,yellow,silver) and black is also allowed
• Video upload and photo upload

```html
<!DOCTYPE html>
<html lang="en">
<head>
<meta charset="utf-8">
<title>Contact — Forge Fitness Hub</title>
<link rel="stylesheet" href="https://fonts.googleapis.com/css2?family=Oswald:wght@500;700&family=Open+Sans:wght@400&family=Montserrat:wght@400;500;600&family=Quicksand:wght@400&family=Roboto:wght@300&display=swap">
<style>
  :root{
    --navy:#0e1c28;
    --navy-deep:#091520;
    --blue:#2e86c1;
    --blue-band:#2f86c3;
    --yellow:#e9b90f;
    --text-grey:#7a7a7a;
    --ink:#1b1b1b;
    --field-bg:#fafafa;
    --field-line:#d9d9d9;
    --map-a:#6e6760;
    --map-b:#5e5a58;
  }
  *{margin:0;padding:0;box-sizing:border-box}
  html,body{width:1014px;height:1200px;overflow:hidden;background:#fff}
  .page{position:relative;width:1014px;height:1200px}

  .site-header{position:absolute;left:0;top:0;width:1014px;height:181px}
  .header-photo{position:absolute;inset:0;background:radial-gradient(ellipse at 50% 40%,#1b3040 0%,var(--navy) 55%,var(--navy-deep) 100%)}
  .brand{position:absolute;left:0;right:0;top:62px;display:flex;justify-content:center;align-items:center;gap:8px}
  .brand-dot{width:14px;height:14px;border-radius:50%;background:var(--blue)}
  .brand-name{font-family:'Oswald',sans-serif;font-weight:700;font-size:15px;letter-spacing:.5px;color:var(--yellow)}
  .main-nav{position:absolute;top:108px;left:0;right:0;font-family:'Oswald',sans-serif;font-weight:500;font-size:13.5px;color:#fff}
  .main-nav a{position:absolute;color:inherit;text-decoration:none;white-space:nowrap;transform:translateX(-50%)}
  .main-nav a.is-current{color:var(--yellow)}

  .contact-title{position:absolute;left:157px;top:198px;font-family:'Oswald',sans-serif;font-weight:700;font-size:56px;line-height:1.2;color:var(--blue);letter-spacing:.5px}
  .contact-intro{position:absolute;left:158px;top:267px;width:700px;font-family:'Open Sans',sans-serif;font-size:10.3px;line-height:15px;color:var(--text-grey)}

  .message-form{position:absolute;left:274px;top:344px;width:466px}
  .form-heading{text-align:center;font-family:'Montserrat',sans-serif;font-weight:500;font-size:11.5px;color:var(--ink);margin-left:-2px}
  .field{position:absolute;left:0;width:466px;background:var(--field-bg);border:1px solid var(--field-line);font-family:'Montserrat',sans-serif;font-size:7.5px;color:#444;padding:6px 8px}
  .field-name{top:42px;height:22px}
  .field-email{top:78px;height:22px}
  .field-message{top:117px;height:83px;padding-top:12px;width:465px}
  .submit-btn{position:absolute;left:195px;top:222px;width:76px;height:26px;background:var(--yellow);color:#fff;font-family:'Montserrat',sans-serif;font-weight:600;font-size:8.5px;letter-spacing:.4px;display:flex;align-items:center;justify-content:center}

  .map-band{position:absolute;left:0;top:665px;width:1014px;height:299px}
  .map-area{position:absolute;inset:0;background:linear-gradient(100deg,var(--map-a) 0%,#66625d 50%,var(--map-b) 100%)}
  .map-cta{position:absolute;left:0;right:0;top:116px;text-align:center}
  .map-cta svg{display:block;margin:0 auto}
  .map-cta-text{font-family:'Quicksand',sans-serif;font-size:27px;color:var(--yellow);margin-top:3px;letter-spacing:.3px}

  .site-footer{position:absolute;left:0;top:964px;width:1014px;height:236px}
  .footer-brand{position:absolute;left:0;right:0;top:94px;display:flex;justify-content:center;align-items:center;gap:8px}
  .social-list{position:absolute;left:456px;top:156px;display:flex;gap:9px}
  .social-item{width:18px;height:18px;border:1px solid #222;border-radius:50%}
  .copyright{position:absolute;left:0;right:0;top:183px;text-align:center;font-family:'Roboto',sans-serif;font-weight:300;font-size:12px;color:#777}
  .footer-band{position:absolute;left:0;bottom:0}
</style>
</head>
<body>
<div class="page">

  <header class="site-header">
    <div class="header-photo" role="img" aria-label="Dark blue-toned photo of an athlete holding dumbbells"></div>
    <div class="brand">
      <span class="brand-dot"></span>
      <span class="brand-name">FORGE FITNESS HUB</span>
    </div>
    <nav class="main-nav">
      <a style="left:300px">HOME</a>
      <a style="left:362px">THE GYM</a>
      <a style="left:445px">THE BOOTCAMP</a>
      <a style="left:546px">PHOTO GALLERY</a>
      <a style="left:634px">ABOUT US</a>
      <a class="is-current" style="left:705px">CONTACT</a>
    </nav>
  </header>

  <h1 class="contact-title">CONTACT US</h1>
  <p class="contact-intro">Sed sollicitudin viverra est, at aliquam metu eratys ultrices tristique massaid.diam purus non velit. Aliquam vel nulla eleifend, consequat elit id, tris- tique massa. Fusce dolor velit, blandit ac erat ac, vestibulum ornare diam. Sed sollicitudin viverra.</p>

  <form class="message-form">
    <h2 class="form-heading">Leave a Message</h2>
    <div class="field field-name">Your name</div>
    <div class="field field-email">Email here</div>
    <div class="field field-message">Write here</div>
    <div class="submit-btn">SUBMIT</div>
  </form>

  <section class="map-band">
    <div class="map-area" role="img" aria-label="Road map of the gym's surrounding region"></div>
    <div class="map-cta">
      <svg width="30" height="37" viewBox="0 0 30 37" aria-hidden="true">
        <path d="M15 0C6.7 0 0 6.7 0 15c0 10 15 22 15 22s15-12 15-22C30 6.7 23.3 0 15 0z" fill="var(--yellow)"/>
        <circle cx="15" cy="14" r="5" fill="#68625c"/>
      </svg>
      <div class="map-cta-text">Make&nbsp; A&nbsp; Contact</div>
    </div>
  </section>

  <footer class="site-footer">
    <div class="footer-brand">
      <span class="brand-dot"></span>
      <span class="brand-name">FORGE FITNESS HUB</span>
    </div>
    <div class="social-list">
      <span class="social-item"></span>
      <span class="social-item"></span>
      <span class="social-item"></span>
      <span class="social-item"></span>
    </div>
    <p class="copyright">Copyright © Forge Fitness Hub 2017. All Rights Reserved | Privacy Policy | Terms of Use</p>
    <svg class="footer-band" width="1014" height="27" viewBox="0 0 1014 27" aria-hidden="true">
      <path d="M0 19H474L506 0L538 19H1014V27H0Z" fill="var(--blue-band)"/>
    </svg>
  </footer>

</div>
</body>
</html>
```